Valcrestaro Car Wrap Design. Hospitality and fashion company on the Alps.

Valcrestaro is an important reality in hospitality and fashion industry with 3 hotels and 5 boutiques in Livigno. Over half a century of history and tradition is their distinctive feature, a guarantee of quality and attention to detail, able to satisfy the most demanding customers.

We have recently developed a new corporate image and now we are ready to enhance our brand visibility by updating and customizing our company VAN.

The Van we want to wrap is a BLACK Halvorn Tessa, lange Version, 2 Schiebetueren (2010). I attached the correct file to work on.

I also attached the new corporate brand-book (logo - colors - font and more).

NB: it is not possible to apply films on the plastic parts. It would be better to avoid that letters and small details go on the areas that have protrusions / recesses.

Industry/Entity Type

Hotel & Fashion

Font styles to use
Other font styles liked:
• BRANDON GROTESQUE

Requirements
Must have
• logo - rhombuses. The Van is BLACK.
Nice to have
• mountains (not mandatory). You can find an example in the uploaded documents.
Should not have
• It is not possible to apply films on the plastic parts. It would be better to avoid that letters and small details go on the areas that have protrusions / recesses.

```html
<!DOCTYPE html>
<html lang="en">
<head>
<meta charset="utf-8">
<title>Valcrestaro – Van Wrap Proposals</title>
<link href="https://fonts.googleapis.com/css2?family=Montserrat:wght@500;600&display=swap" rel="stylesheet">
<style>
  :root {
    --page: #ffffff;
    --van-black: #141414;
    --van-edge: #222222;
    --glass: #1e1f22;
    --glass-front: #3a4d4f;
    --trim: #2b2b2b;
    --tyre: #1a1a1a;
    --rim: #d9dcdf;
    --rim-shade: #a9adb1;
    --brand-green: #1f4d3c;
    --ridge-dark: #5a5a5a;
    --ridge-light: #8f8f8f;
    --ink: #ffffff;
    --ink-soft: #d8d8d8;
    --lamp: #c8242b;
  }
  html, body {
    margin: 0;
    padding: 0;
    width: 1200px;
    height: 1200px;
    overflow: hidden;
    background: var(--page);
  }
  .wrap-sheet { display: block; width: 1200px; height: 1200px; }
  .van-body { fill: var(--van-black); }
  .van-glass { fill: var(--glass); }
  .van-glass-front { fill: var(--glass-front); }
  .van-rail { fill: none; stroke: var(--trim); stroke-width: 5; stroke-linecap: round; }
  .van-seam { fill: none; stroke: #000; stroke-width: 1.5; opacity: .7; }
  .van-lamp { fill: var(--lamp); }
  .van-headlamp { fill: #8e959b; }
  .tyre { fill: var(--tyre); }
  .rim { fill: var(--rim); stroke: var(--rim-shade); stroke-width: 3; }
  .hub { fill: var(--rim-shade); }
  .brand-field { fill: var(--brand-green); }
  .brand-square { fill: var(--van-black); stroke: var(--ink); stroke-width: 3; }
  .brand-square-small { fill: none; stroke: var(--ink); stroke-width: 2.5; }
  .wordmark {
    font-family: "Montserrat", sans-serif;
    font-weight: 500;
    fill: var(--ink);
  }
  .phone {
    font-family: "Montserrat", sans-serif;
    font-weight: 600;
    font-size: 20px;
    letter-spacing: 2px;
    fill: var(--ink);
  }
  .web {
    font-family: "Montserrat", sans-serif;
    font-weight: 600;
    font-size: 12.5px;
    letter-spacing: 1px;
    fill: var(--ink-soft);
  }
</style>
</head>
<body>
<svg class="wrap-sheet" viewBox="0 0 960 960" xmlns="http://www.w3.org/2000/svg">
  <defs>
    <linearGradient id="ridge-tone" x1="0" y1="0" x2="0" y2="1">
      <stop offset="0" stop-color="var(--ridge-light)"/>
      <stop offset="1" stop-color="var(--ridge-dark)"/>
    </linearGradient>
    <g id="van-base">
      <path class="van-body" d="M50,330 C52,290 90,262 200,205 L300,120 C330,100 360,94 420,92 L845,90 C872,94 884,112 888,140 L900,250 L905,360 Q905,374 890,374 L800,374 A65,65 0 0 0 670,374 L235,374 A65,65 0 0 0 105,374 L70,374 Q48,374 48,352 Z"/>
      <path class="van-rail" d="M350,92 L830,86"/>
      <path class="van-glass-front" d="M272,202 L328,118 L418,112 L418,202 Z"/>
      <path class="van-glass" d="M212,212 L262,160 L262,212 Z"/>
      <path class="van-glass" d="M448,108 L645,106 L645,200 L448,203 Z"/>
      <path class="van-glass" d="M655,106 L835,104 Q855,106 858,130 L862,192 L655,196 Z"/>
      <path class="van-seam" d="M255,205 L255,372 M440,105 L440,372 M650,104 L650,372"/>
      <path class="van-lamp" d="M875,120 Q900,170 897,250 L888,255 Q885,180 872,125 Z"/>
      <path class="van-headlamp" d="M58,282 Q75,262 100,260 L96,280 Q75,286 58,292 Z"/>
    </g>
    <g id="van-wheels">
      <circle class="tyre" cx="170" cy="350" r="58"/>
      <circle class="rim" cx="170" cy="350" r="44"/>
      <circle class="hub" cx="170" cy="350" r="9"/>
      <circle class="tyre" cx="735" cy="350" r="58"/>
      <circle class="rim" cx="735" cy="350" r="44"/>
      <circle class="hub" cx="735" cy="350" r="9"/>
    </g>
  </defs>

  <!-- Proposal A: green field with large square panel -->
  <g class="van van-proposal-a" transform="translate(0,0)">
    <use href="#van-base"/>
    <path class="brand-field" d="M545,198 L860,194 L890,230 L903,300 L905,360 Q905,374 890,374 L800,374 A65,65 0 0 0 670,374 L545,374 Z" role="img" aria-label="Brand green panel with fine diamond pattern"/>
    <path d="M245,318 L545,312 L545,374 L235,374 Z" fill="url(#ridge-tone)" role="img" aria-label="Grey mountain ridge silhouette along the lower side"/>
    <text class="wordmark" x="256" y="300" font-size="16.5" letter-spacing="2.6">VALCRESTARO</text>
    <rect class="brand-square" x="492" y="236" width="108" height="108"/>
    <text class="phone" x="677" y="252">0342 555 018</text>
    <text class="web" x="678" y="270">www.valcrestaro.com</text>
    <use href="#van-wheels"/>
  </g>

  <!-- Proposal B: full-length ridge band with wordmark -->
  <g class="van van-proposal-b" transform="translate(0,465)">
    <use href="#van-base"/>
    <path d="M245,312 L900,300 L905,360 Q905,374 890,374 L800,374 A65,65 0 0 0 670,374 L235,374 Z" fill="url(#ridge-tone)" role="img" aria-label="Grey mountain ridge silhouette along the full lower side"/>
    <rect class="brand-square-small" x="270" y="232" width="62" height="62"/>
    <text class="wordmark" x="352" y="272" font-size="26" letter-spacing="4">VALCRESTARO</text>
    <text class="phone" x="677" y="252">0342 555 018</text>
    <text class="web" x="678" y="270">www.valcrestaro.com</text>
    <use href="#van-wheels"/>
  </g>
</svg>
</body>
</html>
```